Picket Sign Advertising For Alaska Tour Company

I would like a relator style picket sign made that I can place by the water near hotels to generate phone calls and website visits. I want to Advertise Our Daily Jet Boat Tours & Jet Ski Tours. This will be a one sided sign. You may be able to see our past brochure and flyer designs and logo. Our FB page is Harlow Summit Excursions and our website is harlowsummitexcursions.com or contact number is 907-518-4463

```html
<!DOCTYPE html>
<html lang="en">
<head>
<meta charset="utf-8">
<title>Harlow Summit Excursions – Picket Sign</title>
<link rel="stylesheet" href="https://fonts.googleapis.com/css2?family=Cinzel:wght@600&family=Montserrat:wght@500;600;700&display=swap">
<style>
  :root {
    --navy: #0d2a6b;
    --gold: #c9a860;
    --gold-light: #e6cf93;
    --white: #ffffff;
    --sky-top: #6f8fb8;
    --sky-mid: #b7c3d3;
    --horizon: #e8a96a;
    --treeline: #1c2026;
    --water: #6d7d8e;
  }
  html, body {
    margin: 0;
    padding: 0;
    width: 1200px;
    height: 800px;
    overflow: hidden;
    background: var(--white);
  }
  .sign {
    position: relative;
    width: 1200px;
    height: 800px;
    overflow: hidden;
  }
  .scene-photo {
    position: absolute;
    inset: 0;
    background:
      linear-gradient(180deg,
        var(--sky-top) 0%,
        var(--sky-mid) 18%,
        #d9c8b4 28%,
        var(--horizon) 31%,
        var(--treeline) 33%,
        #2a3036 42%,
        var(--water) 52%,
        #9aa3ac 60%,
        #3e5a82 75%,
        #2d4b78 100%);
  }
  .band {
    position: absolute;
    inset: 0;
    width: 1200px;
    height: 800px;
  }
  .brand {
    position: absolute;
    left: 36px;
    top: 610px;
    display: flex;
    align-items: center;
    gap: 22px;
  }
  .brand-mark {
    width: 120px;
    height: 120px;
    border-radius: 50%;
    border: 3px solid var(--gold);
    box-sizing: border-box;
    flex: none;
  }
  .brand-text {
    display: flex;
    flex-direction: column;
    width: 340px;
  }
  .brand-name {
    font-family: "Cinzel", serif;
    font-weight: 600;
    font-size: 32px;
    line-height: 1.1;
    color: var(--gold);
    letter-spacing: 2px;
    margin: 0;
  }
  .brand-llc {
    font-family: "Cinzel", serif;
    font-weight: 600;
    font-size: 13px;
    color: var(--gold);
    letter-spacing: 4px;
    border-top: 1.5px solid var(--gold);
    padding-top: 4px;
    margin-top: 6px;
    text-align: right;
  }
  .tagline {
    position: absolute;
    left: 36px;
    top: 746px;
    font-family: "Montserrat", sans-serif;
    font-weight: 500;
    font-size: 14px;
    letter-spacing: 7.4px;
    color: var(--gold-light);
    margin: 0;
    white-space: nowrap;
  }
  .services {
    position: absolute;
    right: 43px;
    top: 676px;
    margin: 0;
    font-family: "Montserrat", sans-serif;
    font-weight: 600;
    font-size: 16px;
    letter-spacing: 2.5px;
    color: var(--gold-light);
    white-space: nowrap;
  }
  .contact {
    position: absolute;
    right: 43px;
    top: 704px;
    display: flex;
    flex-direction: column;
    align-items: flex-start;
    gap: 0;
    font-family: "Montserrat", sans-serif;
    color: var(--white);
  }
  .contact-line {
    display: flex;
    align-items: center;
    gap: 6px;
    white-space: nowrap;
  }
  .contact-web {
    font-weight: 500;
    font-size: 25px;
  }
  .contact-phone {
    font-weight: 700;
    font-size: 48px;
    line-height: 1.1;
    letter-spacing: 0.5px;
  }
  .icon { flex: none; }
</style>
</head>
<body>
<main class="sign">
  <div class="scene-photo" role="img" aria-label="Photo from the bow of a jet boat on a calm river at sunset, spruce treeline silhouetted against an orange and blue sky"></div>

  <svg class="band" viewBox="0 0 1200 800" aria-hidden="true">
    <defs>
      <linearGradient id="gold-edge" x1="0" x2="1" y1="0" y2="0">
        <stop offset="0" stop-color="#b8934a"/>
        <stop offset="0.5" stop-color="#f0d99a"/>
        <stop offset="1" stop-color="#b8934a"/>
      </linearGradient>
    </defs>
    <path d="M0,503 C260,485 520,520 780,605 C900,645 960,668 1030,660 C1110,650 1160,628 1200,612 L1200,800 L0,800 Z" fill="var(--navy)"/>
    <path d="M0,503 C260,485 520,520 780,605 C900,645 960,668 1030,660 C1110,650 1160,628 1200,612" fill="none" stroke="url(#gold-edge)" stroke-width="4"/>
  </svg>

  <div class="brand">
    <div class="brand-mark"></div>
    <div class="brand-text">
      <h1 class="brand-name">Harlow Summit Excursions</h1>
      <span class="brand-llc">LLC</span>
    </div>
  </div>
  <p class="tagline">TAKING YOU WHERE YOU WANT TO GO</p>

  <p class="services">DAILY JET BOAT &amp; JET SKI TOURS</p>

  <div class="contact">
    <div class="contact-line contact-web">
      <svg class="icon" width="22" height="22" viewBox="0 0 24 24" fill="none" stroke="#fff" stroke-width="2">
        <circle cx="12" cy="12" r="10"/>
        <ellipse cx="12" cy="12" rx="4.5" ry="10"/>
        <line x1="2" y1="12" x2="22" y2="12"/>
      </svg>
      <span>www.harlowsummitexcursions.com</span>
    </div>
    <div class="contact-line contact-phone">
      <svg class="icon" width="40" height="40" viewBox="0 0 24 24">
        <circle cx="12" cy="12" r="12" fill="#fff"/>
        <path d="M8.2 6.2c.4-.3 1-.2 1.3.2l1.3 2c.3.4.2 1-.2 1.3l-.8.6c.5 1.3 1.5 2.5 2.8 3.3l.7-.8c.3-.4.9-.5 1.3-.2l2 1.3c.4.3.5.9.2 1.3l-.9 1.2c-.5.6-1.3.8-2 .5-3.2-1.3-5.600-3.8-6.8-7-.3-.7 0-1.5.6-1.9z" fill="var(--navy)"/>
      </svg>
      <span>907-518-4463</span>
    </div>
  </div>
</main>
</body>
</html>
```